Brightwave MolarNet IT Inc. new website

i need a website for my company which is dedicated to installation and service of computer systems in Dental Offices. I would like for it to encompass a technology feel and professional look. The company deals with all aspects of technology like, Audio Visual, computer systems and networks, Cloud services like data backup, data center. We provide manage services, support and services to Dental Professionals.
Updates

Looking for a Technology font but professional look Added Wednesday, April 20, 2016

Target Market(s)

Dental, Dentist

Industry/Entity Type

Dental

Number of Pages Required

5+ page

Font styles to use
Other font styles liked:
• Futuristic or Techy

Colors
0255a3
ec1f27

Requirements
Must have
• Tabs
Nice to have
• Have no idea maybe some suggestion on your part may help
Should not have
• A professional feel but have a techy look

Files

```html
<!DOCTYPE html>
<html lang="en">
<head>
<meta charset="utf-8">
<title>MolarNet IT — Brightwave MolarNet IT Inc.</title>
<link href="https://fonts.googleapis.com/css2?family=Roboto:wght@300;400;500;700&family=Lato:wght@400;700&display=swap" rel="stylesheet">
<style>
:root{
  --brand:#0255a3;
  --brand-dark:#01468a;
  --ink:#222;
  --muted:#8a8a8a;
  --body:#555;
  --panel:#efefef;
  --white:#fff;
  --line:#d6d6d6;
}
*{margin:0;padding:0;box-sizing:border-box}
html,body{width:1200px;height:3516px;overflow:hidden}
body{font-family:'Roboto',sans-serif;color:var(--ink);background:var(--white);position:relative}
section,header,footer{position:absolute;left:0;width:1200px}
.btn{position:absolute;display:flex;align-items:center;justify-content:center;background:var(--brand);color:var(--white);font-size:20px;font-weight:400;text-transform:uppercase;letter-spacing:.3px}
.btn.light{background:var(--white);color:var(--brand)}
.section-title{position:absolute;left:0;width:1200px;text-align:center;font-size:42px;font-weight:400;color:var(--brand);text-transform:uppercase}
.section-title b{font-weight:700}

/* header */
.site-header{top:0;height:122px;border-bottom:3px solid var(--brand);background:var(--white)}
.brand{position:absolute;left:80px;top:36px;display:flex;align-items:center;gap:14px;font-size:40px;font-weight:700;color:var(--brand)}
.brand .mark{width:36px;height:36px;background:var(--brand)}
.search{position:absolute;left:843px;top:12px;width:277px;height:40px;border:1px solid #e2e2e2;display:flex;align-items:center;padding:0 12px;font-size:14px;color:#aaa}
.search svg{position:absolute;right:10px;top:9px}
.main-nav{position:absolute;right:80px;top:72px;display:flex;gap:44px;font-size:16px;color:#444}
.main-nav .active{color:var(--brand)}

/* hero */
.hero{top:122px;height:555px}
.hero-photo{position:absolute;inset:0;background:linear-gradient(90deg,#f4f6f8 0%,#e9edf1 40%,#b9c9d8 70%,#8aa5bf 100%)}
.hero-title{position:absolute;left:80px;top:228px;font-family:'Lato',sans-serif;font-size:52px;font-weight:700;color:var(--brand)}
.hero-sub{position:absolute;left:80px;top:300px;font-family:'Lato',sans-serif;font-size:21px;color:var(--brand)}
.hero .btn{left:80px;top:347px;width:232px;height:61px}

/* welcome */
.welcome{top:677px;height:389px}
.welcome .section-title{top:60px}
.welcome-text{position:absolute;left:170px;width:860px;top:126px;text-align:center;font-size:14px;line-height:26.5px;color:var(--muted)}
.welcome .btn{left:515px;top:265px;width:169px;height:61px}

/* services */
.services{top:1066px;height:594px;background:var(--panel)}
.services .section-title{top:57px}
.service{position:absolute;top:136px;width:330px;text-align:center}
.service-photo{width:205px;height:157px;margin:0 auto;border:2px solid var(--brand);border-radius:10px;background:linear-gradient(135deg,#d8e6f3,#6f9cc8)}
.service-name{margin-top:22px;height:60px;font-size:21px;color:var(--brand);text-transform:uppercase;line-height:25px}
.service-text{font-size:14.5px;line-height:23px;color:var(--body)}
.service .btn{position:relative;margin:24px auto 0;width:169px;height:59px}

/* support */
.support{top:1660px;height:347px;background:var(--brand);color:var(--white);text-align:center}
.support h2{position:absolute;top:60px;width:100%;font-size:41px;font-weight:400;text-transform:uppercase}
.support .lead{position:absolute;top:125px;width:100%;font-size:24px}
.support .contact-line{position:absolute;top:172px;width:100%;font-size:19px}
.support .btn{left:504px;top:227px;width:192px;height:59px}

/* blog */
.blog{top:2007px;height:614px;background:var(--panel)}
.blog .section-title{top:60px}
.post{position:absolute;top:133px;width:251px}
.post-photo{height:169px;background:linear-gradient(135deg,#e9eef3,#b4c4d4)}
.post-date{margin-top:22px;font-size:15px;color:var(--brand)}
.post-title{margin-top:18px;font-size:15px;line-height:22px;text-transform:uppercase;color:var(--ink)}
.post-text{margin-top:9px;font-size:14px;line-height:22px;color:var(--body)}
.post .btn{position:relative;margin-top:20px;width:171px;height:61px}

/* testimonials */
.testimonials{top:2621px;height:520px;background:var(--white)}
.testimonials .section-title{top:60px}
.quote-badge{position:absolute;left:569px;top:133px}
.quote-text{position:absolute;left:260px;width:680px;top:228px;text-align:center;font-size:14.5px;line-height:25px;color:var(--muted)}
.client-name{position:absolute;top:320px;width:100%;text-align:center;font-size:16px;color:var(--brand);text-transform:uppercase}
.avatar{position:absolute;border-radius:50%;background:radial-gradient(circle at 50% 40%,#d9c6b4,#8f7d6c)}

/* footer */
.site-footer{top:3141px;height:312px;background:var(--panel)}
.footer-col{position:absolute;top:42px;width:240px}
.footer-col h3{font-size:19px;font-weight:400;color:var(--brand);margin-bottom:20px}
.footer-brand{display:flex;align-items:center;gap:10px;font-size:30px;font-weight:700;color:var(--brand);margin-top:28px}
.footer-brand .mark{width:26px;height:26px;background:var(--brand)}
.social{display:flex;gap:10px;margin:30px 0 0 16px}
.social span{width:42px;height:42px;border-radius:50%;background:var(--brand)}
.news-item{display:flex;gap:14px;margin-bottom:20px}
.news-thumb{width:48px;height:48px;border-radius:50%;background:radial-gradient(circle,#c9b39c,#6d5b4a);flex:none}
.news-item p{font-size:14px;line-height:21px;color:var(--body)}
.field{width:230px;height:35px;border:1px solid var(--line);background:var(--white);font-size:12px;color:#999;padding:9px 8px;margin-bottom:6px}
.field.tall{height:61px}
.send{width:230px;height:35px;background:var(--brand);color:var(--white);font-size:14px;text-transform:uppercase;display:flex;align-items:center;justify-content:center}
.touch-item{display:flex;gap:16px;font-size:14px;line-height:20px;color:var(--body);margin-bottom:16px;align-items:flex-start}
.touch-item svg{flex:none}
.copyright{top:3453px;height:63px;background:var(--brand);color:var(--white);display:flex;align-items:center;justify-content:center;font-size:14px}
.copyright b{margin:0 5px}
</style>
</head>
<body>

<header class="site-header">
  <div class="brand"><span class="mark"></span>MolarNet IT</div>
  <div class="search">Search
    <svg width="22" height="22" viewBox="0 0 22 22"><circle cx="9" cy="9" r="6.5" fill="none" stroke="#0255a3" stroke-width="2.5"/><line x1="14" y1="14" x2="20" y2="20" stroke="#0255a3" stroke-width="3" stroke-linecap="round"/></svg>
  </div>
  <nav class="main-nav">
    <span class="active">HOME</span><span>ABOUT</span><span>SERVICES</span><span>SUPPORT</span><span>CLIENT</span><span>BLOG</span><span>CONTACT</span>
  </nav>
</header>

<section class="hero">
  <div class="hero-photo" role="img" aria-label="Dental IT technician in blue scrubs reviewing paperwork in a bright office"></div>
  <h1 class="hero-title">MOLARNET IT</h1>
  <p class="hero-sub">Lorem ipsum dolor amet simple dummy text&nbsp; for print.</p>
  <span class="btn">Contact now us</span>
</section>

<section class="welcome">
  <h2 class="section-title">Welcome to <b>MolarNet IT</b></h2>
  <p class="welcome-text">Lorem Ipsum is simply dummy text of the printing and typesetting industry. Lorem Ipsum has been the industry's standard dummy text ever since the 1500s, when an unknown printer took a galley of type and scrambled it to make a type specimen book. It has survived not only five centuries, but also the leap into electronic typesetting, remaining essentially unchanged. It was popularised in the 1960s with the release of Letraset sheets containing Lorem Ipsum passages, and more recently with desktop publishing software like Aldus PageMaker including versions of Lorem Ipsum.</p>
  <span class="btn">Know more</span>
</section>

<section class="services">
  <h2 class="section-title">Our <b>Services</b></h2>
  <div class="service" style="left:79px">
    <div class="service-photo" role="img" aria-label="Meeting room with a projected presentation"></div>
    <h3 class="service-name">Audio Visual</h3>
    <p class="service-text">Lorem Ipsum is simply dummy text of the printing and typesetting industry. Lorem Ipsum has been the industry's standard dummy.</p>
    <span class="btn">Read more</span>
  </div>
  <div class="service" style="left:435px">
    <div class="service-photo" role="img" aria-label="Networked laptops linked by data streams"></div>
    <h3 class="service-name">Computer systems and<br>networks</h3>
    <p class="service-text">Lorem Ipsum is simply dummy text of the printing and typesetting industry. Lorem Ipsum has been the industry's standard dummy.</p>
    <span class="btn">Read more</span>
  </div>
  <div class="service" style="left:791px">
    <div class="service-photo" role="img" aria-label="File folders floating around a computer for cloud backup"></div>
    <h3 class="service-name">Cloud services of data<br>backup</h3>
    <p class="service-text">Lorem Ipsum is simply dummy text of the printing and typesetting industry. Lorem Ipsum has been the industry's standard dummy.</p>
    <span class="btn">Read more</span>
  </div>
</section>

<section class="support">
  <h2>Support with us</h2>
  <p class="lead">Got unanswered questions? We are Ready to Help You</p>
  <p class="contact-line">email : info@molarnetit.com | Call: +(91) 555 010 2290</p>
  <span class="btn light">Contact now</span>
</section>

<section class="blog">
  <h2 class="section-title">Latest <b>Blog</b></h2>
  <article class="post" style="left:77px">
    <div class="post-photo" role="img" aria-label="Support agent with headset holding a tablet"></div>
    <p class="post-date">Posted by April, 21</p>
    <h3 class="post-title">Lorem ipsum dolor amet<br>simple text</h3>
    <p class="post-text">Lorem Ipsum is simply dummy text of the printing and typesetting industry.</p>
    <span class="btn">Read more</span>
  </article>
  <article class="post" style="left:342px">
    <div class="post-photo" role="img" aria-label="Dental team smiling in a clinic"></div>
    <p class="post-date">Posted by April, 21</p>
    <h3 class="post-title">Lorem ipsum dolor amet<br>simple text</h3>
    <p class="post-text">Lorem Ipsum is simply dummy text of the printing and typesetting industry.</p>
    <span class="btn">Read more</span>
  </article>
  <article class="post" style="left:607px">
    <div class="post-photo" role="img" aria-label="Technician working at computer screens in a blue lab"></div>
    <p class="post-date">Posted by April, 21</p>
    <h3 class="post-title">Lorem ipsum dolor amet<br>simple text</h3>
    <p class="post-text">Lorem Ipsum is simply dummy text of the printing and typesetting industry.</p>
    <span class="btn">Read more</span>
  </article>
  <article class="post" style="left:872px">
    <div class="post-photo" role="img" aria-label="Dentist standing in a modern treatment room"></div>
    <p class="post-date">Posted by April, 21</p>
    <h3 class="post-title">Lorem ipsum dolor amet<br>simple text</h3>
    <p class="post-text">Lorem Ipsum is simply dummy text of the printing and typesetting industry.</p>
    <span class="btn">Read more</span>
  </article>
</section>

<section class="testimonials">
  <h2 class="section-title">What our <b>client say</b></h2>
  <svg class="quote-badge" width="62" height="62" viewBox="0 0 62 62"><circle cx="31" cy="31" r="29.5" fill="#fff" stroke="#0255a3" stroke-width="2"/><path d="M20 36v-6c0-5 3-8 7-9v3c-2 1-3 3-3 5h3v7zM33 36v-6c0-5 3-8 7-9v3c-2 1-3 3-3 5h3v7z" fill="#0255a3"/></svg>
  <p class="quote-text">" Lorem Ipsum is simply dummy text of the printing and typesetting industry. Lorem Ipsum has been the industry's standard dummy text ever since the 1500s, when an unknown printer took a galley of type and scrambled it to make a type specimen book. It has survived "</p>
  <p class="client-name">Client name</p>
  <div class="avatar" style="left:454px;top:371px;width:82px;height:82px" role="img" aria-label="Client portrait"></div>
  <div class="avatar" style="left:555px;top:366px;width:90px;height:90px;border:3px solid #0255a3" role="img" aria-label="Client portrait"></div>
  <div class="avatar" style="left:664px;top:371px;width:82px;height:82px" role="img" aria-label="Client portrait"></div>
</section>

<footer class="site-footer">
  <div class="footer-col" style="left:80px">
    <h3>About</h3>
    <div class="footer-brand"><span class="mark"></span>MolarNet IT</div>
    <div class="social" aria-label="Social links"><span></span><span></span><span></span><span></span></div>
  </div>
  <div class="footer-col" style="left:342px">
    <h3>Latest News</h3>
    <div class="news-item"><div class="news-thumb" role="img" aria-label="News thumbnail"></div><p>19/4<br>Lorem ipsum dolor sit<br>amet, consectetur adip...</p></div>
    <div class="news-item"><div class="news-thumb" role="img" aria-label="News thumbnail"></div><p>19/4<br>Lorem ipsum dolor sit<br>amet, consectetur adip...</p></div>
  </div>
  <div class="footer-col" style="left:607px">
    <h3>Contact Us</h3>
    <div class="field">Name</div>
    <div class="field">E-Mail</div>
    <div class="field tall">Message</div>
    <div class="send">Send</div>
  </div>
  <div class="footer-col" style="left:866px">
    <h3>Keep in Touch</h3>
    <div class="touch-item"><svg width="22" height="28" viewBox="0 0 22 28"><path d="M11 2a8 8 0 0 0-8 8c0 6 8 16 8 16s8-10 8-16a8 8 0 0 0-8-8z" fill="none" stroke="#0255a3" stroke-width="2"/><circle cx="11" cy="10" r="3" fill="none" stroke="#0255a3" stroke-width="2"/></svg><span>MOLARNET IT<br>Lorem ipsum dolor amet simple.</span></div>
    <div class="touch-item"><svg width="22" height="22" viewBox="0 0 22 22"><path d="M5 2l4 4-2 3c1 3 3 5 6 6l3-2 4 4-3 3C10 20 2 12 2 5z" fill="none" stroke="#0255a3" stroke-width="1.8" stroke-linejoin="round"/></svg><span>+(91) 555 010 2290</span></div>
    <div class="touch-item"><svg width="22" height="22" viewBox="0 0 22 22"><rect x="6" y="2" width="10" height="5" fill="none" stroke="#0255a3" stroke-width="1.8"/><rect x="2" y="7" width="18" height="9" rx="1" fill="none" stroke="#0255a3" stroke-width="1.8"/><rect x="6" y="13" width="10" height="7" fill="#fff" stroke="#0255a3" stroke-width="1.8"/></svg><span>+(91) 555 010 2290</span></div>
    <div class="touch-item"><svg width="22" height="18" viewBox="0 0 22 18"><rect x="1" y="2" width="20" height="14" fill="none" stroke="#0255a3" stroke-width="1.8"/><path d="M1 2l10 8 10-8" fill="none" stroke="#0255a3" stroke-width="1.8"/></svg><span>info@molarnetit.com</span></div>
  </div>
</footer>

<footer class="copyright">© 2016 <b>MOLARNET IT</b> All rights reserved.</footer>

</body>
</html>
```